Website design for commercial and residential security company

we're looking to see some new designs for an established company with no website.

homepage and one inner page

here is a link to the homepage content, sitemap, logo and more.
https://files.brontavel.net/share/7QxmPzLrTw2vNkdJhYcsa9eFgbUoiVwRn?view=open

call to action should be Request A Quote

if you have any questions please send them to us asap

thank you

1 page

Sans Serif

```html
<!DOCTYPE html>
<html lang="en">
<head>
<meta charset="utf-8">
<title>Ridgeway Security Group</title>
<link href="https://fonts.googleapis.com/css2?family=Montserrat:wght@500;600;700;800&family=Raleway:wght@400;500;600;700&display=swap" rel="stylesheet">
<style>
:root{
  --navy:#0f2a80;
  --navy-deep:#0a1d5c;
  --gold:#d3ab35;
  --ink:#1d1d1d;
  --dark:#222222;
  --black:#121212;
  --tile:#3c3c3c;
  --light:#f6f6f6;
  --text:#2b2b2b;
  --white:#ffffff;
}
*{box-sizing:border-box;margin:0;padding:0}
html,body{width:1200px;height:3142px;overflow:hidden}
body{position:relative;background:var(--white);font-family:"Raleway",sans-serif;color:var(--text)}
.abs{position:absolute}
.heading{font-family:"Montserrat",sans-serif}

/* brand: plain name with one square */
.brand{display:flex;align-items:center;gap:10px;font-family:"Montserrat",sans-serif;font-weight:700;line-height:1;white-space:nowrap}
.brand-mark{width:14px;height:14px;flex:none}

/* hero */
.hero{left:0;top:0;width:1200px;height:500px;background:radial-gradient(circle at 560px 210px,#2a4db0 0,#173a9e 30%,var(--navy) 60%,var(--navy-deep) 100%)}
.hero-camera{left:740px;top:92px;width:460px;height:408px;background:linear-gradient(140deg,#f4f4f6 0,#d9dbe2 45%,#8f97b4 100%);border-radius:60px 0 0 0;opacity:.92}
.brand-header{left:100px;top:44px;font-size:20px;color:var(--white)}
.brand-header .brand-mark{background:var(--gold)}
.topbar{top:14px;right:100px;display:flex;align-items:center;gap:18px;color:var(--white);font-size:12px;font-weight:500}
.topbar span{display:flex;align-items:center;gap:6px}
.social-sq{width:12px;height:12px;background:var(--white);border-radius:2px}
.social-sq.gold{width:20px;height:20px;background:var(--gold)}
.nav{top:54px;left:544px;display:flex;gap:22px;font-family:"Montserrat",sans-serif;font-size:11.5px;font-weight:600;color:var(--white)}
.nav .active{color:var(--gold);border-bottom:2px solid var(--gold);padding-bottom:3px}
.btn-quote{left:956px;top:48px;width:146px;height:27px;background:var(--gold);color:var(--ink);font-family:"Montserrat",sans-serif;font-weight:700;font-size:11.5px;display:flex;align-items:center;justify-content:center;border-radius:2px}
.hero-title{left:112px;top:188px;font-size:31px;font-weight:800;color:var(--white)}
.hero-sub{left:113px;top:233px;width:330px;font-size:12.5px;font-weight:600;color:var(--white);line-height:18px}
.hero-sub em{font-style:normal;color:var(--gold)}
.btn-outline-light{left:113px;top:290px;width:104px;height:31px;border:1px solid var(--white);color:var(--white);font-family:"Montserrat",sans-serif;font-size:10.5px;font-weight:700;display:flex;align-items:center;justify-content:center;border-radius:2px}
.hero-curve{left:0;top:410px}

/* about */
.photo{border-radius:2px}
.about-photo-a{left:98px;top:576px;width:206px;height:211px;background:linear-gradient(135deg,#c9b7a4,#9ea6b3 60%,#7d8594)}
.about-photo-b{left:310px;top:576px;width:205px;height:367px;background:linear-gradient(160deg,#e6e6e6,#b9b6b4 55%,#6c6a6a)}
.trusted{left:98px;top:792px;width:206px;height:151px;background:var(--navy);color:var(--white);font-family:"Montserrat",sans-serif;font-weight:700;font-size:23px;line-height:30px;text-align:center;display:flex;align-items:center;justify-content:center}
.trusted b{color:var(--gold)}
.about-title{left:588px;top:590px;font-size:28px;font-weight:800;color:var(--gold)}
.about-text{left:588px;top:640px;width:490px;font-size:12px;line-height:18px;font-weight:500}
.about-text p{margin-bottom:14px}
.mission-title{font-family:"Montserrat",sans-serif;font-size:15px;font-weight:700;color:var(--navy);margin:20px 0 10px}
.about-text .strong{font-weight:700;color:var(--ink)}
.btn-gold{left:589px;top:891px;width:102px;height:31px;background:var(--gold);color:var(--ink);font-family:"Montserrat",sans-serif;font-size:10px;font-weight:700;display:flex;align-items:center;justify-content:center;border-radius:2px}

/* solutions */
.solutions{left:0;top:1018px;width:1200px;height:826px;background:var(--light)}
.section-title{width:1200px;left:0;text-align:center;font-family:"Montserrat",sans-serif;font-weight:800;font-size:26px}
.solutions-title{top:1088px;color:var(--gold)}
.sol-card{top:1159px;height:240px}
.sol-commercial{left:0;width:596px;background:linear-gradient(120deg,#1d4aa0,#3d8fd6 45%,#0d3070)}
.sol-residential{left:604px;width:596px;background:linear-gradient(120deg,#f1d48a,#d69b45 50%,#b9c7d6)}
.sol-label{top:1359px;height:40px;display:flex;align-items:center;justify-content:center;font-family:"Montserrat",sans-serif;font-weight:700;font-size:18px}
.label-commercial{left:0;width:596px;background:var(--black);color:var(--gold)}
.label-residential{left:604px;width:596px;background:var(--gold);color:var(--ink)}
.pointer{left:278px;top:1398px;width:0;height:0;border-left:20px solid transparent;border-right:20px solid transparent;border-top:18px solid var(--black)}
.tile{width:131px;height:100px;background:var(--tile);border-radius:3px;color:var(--white);font-size:12.5px;font-weight:600;display:flex;flex-direction:column;align-items:center;justify-content:flex-end;padding-bottom:12px;gap:10px}
.tile svg{width:38px;height:38px}
.sol-head{left:510px;top:1468px;width:520px;font-family:"Montserrat",sans-serif;font-size:15px;font-weight:700;line-height:21px;color:var(--gold)}
.sol-text{left:510px;top:1524px;width:530px;font-size:12px;line-height:19px;font-weight:500}
.sol-text ul{list-style:none;margin-top:10px}
.sol-text li{position:relative;padding-left:14px}
.sol-text li::before{content:"";position:absolute;left:0;top:6px;border-left:5px solid var(--gold);border-top:4px solid transparent;border-bottom:4px solid transparent}
.btn-outline-gold{left:510px;top:1738px;width:104px;height:31px;border:1px solid var(--gold);color:var(--gold);font-family:"Montserrat",sans-serif;font-size:10px;font-weight:600;display:flex;align-items:center;justify-content:center;border-radius:2px;background:var(--white)}

/* resources */
.resources{left:0;top:1844px;width:1200px;height:504px;background:var(--dark)}
.resources-title{top:1912px;color:var(--white)}
.person{top:1984px;width:202px;height:195px;border:3px solid #e8e8e8;background:linear-gradient(180deg,#dcdcdc,#9a9a9a)}
.person.active{border-color:#1d4aa8}
.person-name{top:2198px;width:202px;text-align:center;color:#e6e6e6;font-size:13.5px;font-weight:600}
.round-icon{top:2162px;width:30px;height:30px;border-radius:50%;display:flex;align-items:center;justify-content:center}
.arrow{top:2070px;width:24px;height:24px}
.btn-view{left:549px;top:2251px;width:103px;height:30px;border:1px solid var(--gold);color:var(--white);font-family:"Montserrat",sans-serif;font-size:10px;font-weight:600;display:flex;align-items:center;justify-content:center;border-radius:2px}

/* package */
.brand-center{left:0;width:1200px;top:2422px;justify-content:center;font-size:24px;color:var(--ink)}
.brand-center .brand-mark{background:var(--gold)}
.package{left:285px;top:2504px;width:628px;height:229px;background:var(--white);box-shadow:0 2px 18px rgba(0,0,0,.09);border-radius:3px;text-align:center}
.pkg-title{position:absolute;left:0;width:100%;top:28px;color:var(--gold);font-size:16px;font-weight:600}
.pkg-price{position:absolute;left:0;width:100%;top:50px;color:var(--gold);font-family:"Montserrat",sans-serif;font-size:25px;font-weight:700}
.pkg-inc{position:absolute;left:0;width:100%;top:96px;color:var(--gold);font-size:16px;font-weight:500}
.pkg-inc span{display:inline-block;width:26px;height:1px;background:var(--gold);vertical-align:middle;margin:0 8px}
.pkg-line{position:absolute;left:0;width:100%;font-size:14px;color:var(--ink);font-weight:500}

/* footer */
.footer{left:0;top:2793px;width:1200px;height:314px;background:var(--black)}
.footer-curve{left:0;top:2786px}
.footer-brand{left:98px;top:2990px;font-size:14px;color:var(--white);flex-direction:column;gap:8px;text-align:center;line-height:18px}
.footer-brand .brand-mark{background:var(--gold)}
.ft-head{top:2872px;color:var(--gold);font-size:17px;font-weight:600}
.ft-links{left:247px;top:2914px;color:var(--white);font-size:12px;line-height:28px;font-weight:500}
.ft-links .current{text-decoration:underline;color:var(--gold)}
.ft-contact{left:422px;top:2914px;color:var(--white);font-size:12px;font-weight:500}
.ft-contact .label{color:var(--gold);font-size:11px;margin-bottom:8px}
.ft-contact .row{display:flex;align-items:center;gap:8px;margin-bottom:8px}
.field{background:#262626;color:#7d7d7d;font-size:12px;display:flex;align-items:center;gap:8px;padding:0 12px;border-radius:2px}
.field-col{left:649px;width:218px;height:30px}
.field-comments{left:894px;top:2913px;width:207px;height:116px;align-items:flex-start;padding-top:9px}
.btn-submit{left:649px;top:3045px;width:92px;height:28px;border:1px solid var(--white);color:var(--white);font-size:12px;font-weight:600;display:flex;align-items:center;justify-content:center;border-radius:2px}
.copyright{left:0;top:3107px;width:1200px;height:35px;background:var(--gold);color:var(--ink);font-size:11px;font-weight:500;display:flex;align-items:center;justify-content:space-between;padding:0 100px}
.copyright .socials{display:flex;gap:10px}
.copyright .socials i{width:10px;height:10px;background:var(--ink);border-radius:2px;display:block}
</style>
</head>
<body>

<!-- HERO -->
<div class="abs hero" role="img" aria-label="Deep blue backdrop of a modern building facade with a digital security overlay"></div>
<div class="abs hero-camera" role="img" aria-label="White outdoor surveillance camera mounted on a wall bracket"></div>

<div class="abs brand brand-header"><span class="brand-mark"></span>Ridgeway Security Group</div>

<div class="abs topbar">
  <span><svg width="12" height="12" viewBox="0 0 24 24"><path fill="#d3ab35" d="M6.6 10.8a15 15 0 006.6 6.6l2.2-2.2c.3-.3.7-.4 1-.2 1.1.4 2.3.6 3.6.6.6 0 1 .4 1 1V20c0 .6-.4 1-1 1C10.6 21 3 13.4 3 4c0-.6.4-1 1-1h3.5c.6 0 1 .4 1 1 0 1.3.2 2.5.6 3.6.1.3 0 .7-.2 1z"/></svg>555-014-7720</span>
  <span><svg width="14" height="11" viewBox="0 0 24 18"><rect x="1" y="1" width="22" height="16" fill="none" stroke="#d3ab35" stroke-width="2"/><path d="M1 1l11 9 11-9" fill="none" stroke="#d3ab35" stroke-width="2"/></svg>info@ridgewaysecurity.example</span>
  <i class="social-sq"></i>
  <i class="social-sq gold"></i>
</div>

<nav class="abs nav">
  <span class="active">HOME</span><span>ABOUT US</span><span>SOLUTIONS</span><span>RESOURCES</span><span>CONTACT US</span>
</nav>
<div class="abs btn-quote">REQUEST A QUOTE</div>

<h1 class="abs heading hero-title">HIGHEST LEVEL SECURITY</h1>
<p class="abs hero-sub">Ridgeway Security Group is a <em>privately owned family company</em></p>
<div class="abs btn-outline-light">READ MORE</div>

<svg class="abs hero-curve" width="1200" height="110" viewBox="0 0 1200 110">
  <path d="M0 84 L440 84 Q560 84 600 12 Q640 84 760 84 L1200 84 L1200 110 L0 110 Z" fill="#fff"/>
  <path d="M0 84 L440 84 Q560 84 600 12 Q640 84 760 84 L1200 84" fill="none" stroke="#d3ab35" stroke-width="6"/>
</svg>

<!-- ABOUT -->
<div class="abs photo about-photo-a" role="img" aria-label="Technician installing a security camera"></div>
<div class="abs photo about-photo-b" role="img" aria-label="Hand holding a phone showing live home camera feeds"></div>
<div class="abs trusted"><div>We're Trusted<br>by morethan<br><b>2865</b> Clients</div></div>

<h2 class="abs heading about-title">ABOUT US</h2>
<div class="abs about-text">
  <p>Ridgeway Security Group is a privately owned family company that specializes in residential, small businesses, large warehouse/office buildings installations of high end physical security products.</p>
  <p>We provide all types of Closed Circuit Television, Card Access, Burglar, residential fire, residential IT Systems, Residential/Commercial Audio, Home Theater and automation.</p>
  <h3 class="mission-title">OUR MISSION</h3>
  <p class="strong">To provide our customers with comprehensive security, audio/video, and automation with top notch customer service. We Ensure Security with Smart Tools.</p>
  <p>The graded security measures from Ridgeway Security Group...</p>
</div>
<div class="abs btn-gold">READ MORE</div>

<!-- SOLUTIONS -->
<div class="abs solutions"></div>
<h2 class="abs section-title solutions-title">SOLUTIONS</h2>
<div class="abs sol-card sol-commercial" role="img" aria-label="Shopping mall escalators with a dome security camera"></div>
<div class="abs sol-card sol-residential" role="img" aria-label="Sunlit house with wireless security cameras"></div>
<div class="abs sol-label label-commercial">Commercial Solutions</div>
<div class="abs sol-label label-residential">Residential Security Solutions</div>
<div class="abs pointer"></div>

<div class="abs tile" style="left:184px;top:1470px">
  <svg viewBox="0 0 40 40" fill="none" stroke="#fff" stroke-width="2.5"><path d="M6 12l20 8-4 7-18-8z" fill="#fff"/><path d="M26 22l6 3M33 20v14M28 34h8"/></svg>CCTV</div>
<div class="abs tile" style="left:330px;top:1470px">
  <svg viewBox="0 0 40 40" fill="none" stroke="#fff" stroke-width="2"><rect x="4" y="4" width="32" height="32" rx="4"/><path d="M20 10a9 9 0 019 9v6M11 19a9 9 0 015-8M20 15a4 4 0 014 4v9M16 19v8M20 20v12"/></svg>Access Control</div>
<div class="abs tile" style="left:184px;top:1585px">
  <svg viewBox="0 0 40 40" fill="none" stroke="#fff" stroke-width="2.5"><circle cx="20" cy="22" r="12"/><path d="M20 15v7l5 3M6 10l6-5M34 10l-6-5M12 34l-3 4M28 34l3 4"/></svg>Alarm</div>
<div class="abs tile" style="left:330px;top:1585px">
  <svg viewBox="0 0 40 40" fill="none" stroke="#fff" stroke-width="2.5"><rect x="5" y="10" width="20" height="24"/><circle cx="15" cy="26" r="4"/><path d="M22 14l12-6v16M22 30l12-6"/></svg>Audio / Video</div>

<h3 class="abs sol-head">Protect assets and security of your business with Exceptional Commercial Security Installation</h3>
<div class="abs sol-text">
  <p>People's safety is our top priority. This includes ensuring that the security system built at your commercial property is configured accurately. Further, it will protect against intruders, burglaries, and holdups. We do this by:</p>
  <ul>
    <li>Audio &amp; Video Solutions for your commercial property</li>
    <li>Burglar Alarms &amp; Detectors</li>
    <li>CCTV cameras equipped with facial recognition technologies enable the technology to identify the offenders.</li>
    <li>Monitoring of alarms and video recordings 24 hours a day, seven days a week. Addressing all the incidents with an urgent response.</li>
  </ul>
</div>
<div class="abs btn-outline-gold">READ MORE</div>

<!-- RESOURCES -->
<div class="abs resources"></div>
<h2 class="abs section-title resources-title">RESOURCES</h2>
<svg class="abs arrow" style="left:108px" viewBox="0 0 24 24"><path d="M15 4l-8 8 8 8" fill="none" stroke="#bbb" stroke-width="3"/></svg>
<svg class="abs arrow" style="left:1070px" viewBox="0 0 24 24"><path d="M9 4l8 8-8 8" fill="none" stroke="#fff" stroke-width="3"/></svg>

<div class="abs person" style="left:161px" role="img" aria-label="Portrait of team member Daniel Hartley"></div>
<div class="abs person" style="left:386px" role="img" aria-label="Portrait of team member Owen Mercer"></div>
<div class="abs person" style="left:611px" role="img" aria-label="Portrait of team member Nina Calder"></div>
<div class="abs person active" style="left:836px" role="img" aria-label="Portrait of team member Lucas Brandt"></div>
<div class="abs round-icon" style="left:905px;background:#1d4aa8"><svg width="13" height="13" viewBox="0 0 24 24"><path fill="#fff" d="M6.6 10.8a15 15 0 006.6 6.6l2.2-2.2c.3-.3.7-.4 1-.2 1.1.4 2.3.6 3.6.6.6 0 1 .4 1 1V20c0 .6-.4 1-1 1C10.6 21 3 13.4 3 4c0-.6.4-1 1-1h3.5c.6 0 1 .4 1 1 0 1.3.2 2.5.6 3.6.1.3 0 .7-.2 1z"/></svg></div>
<div class="abs round-icon" style="left:940px;background:var(--gold)"><svg width="13" height="11" viewBox="0 0 24 18"><rect x="2" y="2" width="20" height="14" fill="none" stroke="#fff" stroke-width="2.5"/><path d="M2 2l10 8 10-8" fill="none" stroke="#fff" stroke-width="2.5"/></svg></div>

<div class="abs person-name" style="left:161px">Daniel Hartley</div>
<div class="abs person-name" style="left:386px">Owen Mercer</div>
<div class="abs person-name" style="left:611px">Nina Calder</div>
<div class="abs person-name" style="left:836px">Lucas Brandt</div>
<div class="abs btn-view">VIEW ALL</div>

<!-- PACKAGE -->
<div class="abs brand brand-center"><span class="brand-mark"></span>Ridgeway Security Group</div>
<div class="abs package">
  <div class="pkg-title">Basic Security Package</div>
  <div class="pkg-price">$1,1999.99</div>
  <div class="pkg-inc"><span></span>Includes<span></span></div>
  <div class="pkg-line" style="top:120px">3 motion detectors, 3 door contacts,&nbsp; Keypad/control Panel</div>
  <div class="pkg-line" style="top:151px;color:var(--gold);font-size:16px">Automation &amp; security add ans are available</div>
  <div class="pkg-line" style="top:175px;font-size:16px">$30 per month for monitoring and remote control of system</div>
</div>

<!-- FOOTER -->
<div class="abs footer"></div>
<svg class="abs footer-curve" width="1200" height="100" viewBox="0 0 1200 100">
  <path d="M0 0 L1200 0 L1200 10 L760 10 Q640 10 600 86 Q560 10 440 10 L0 10 Z" fill="#fff"/>
  <path d="M0 10 L440 10 Q560 10 600 86 Q640 10 760 10 L1200 10" fill="none" stroke="#d3ab35" stroke-width="6"/>
</svg>
<div class="abs brand footer-brand"><span class="brand-mark"></span><div>Ridgeway<br>Security</div></div>

<div class="abs ft-head" style="left:247px">Quick Link</div>
<div class="abs ft-head" style="left:422px">Conatct info</div>
<div class="abs ft-head" style="left:648px">Quick Inquiry</div>

<div class="abs ft-links">
  <div class="current">Home</div><div>About Us</div><div>Solutions</div><div>Resources</div><div>Contact Us</div>
</div>

<div class="abs ft-contact">
  <div class="label">CALL US:</div>
  <div class="row"><svg width="12" height="12" viewBox="0 0 24 24"><path fill="#d3ab35" d="M6.6 10.8a15 15 0 006.6 6.6l2.2-2.2c.3-.3.7-.4 1-.2 1.1.4 2.3.6 3.6.6.6 0 1 .4 1 1V20c0 .6-.4 1-1 1C10.6 21 3 13.4 3 4c0-.6.4-1 1-1h3.5c.6 0 1 .4 1 1 0 1.3.2 2.5.6 3.6.1.3 0 .7-.2 1z"/></svg>555-014-7720</div>
  <div class="row"><svg width="13" height="10" viewBox="0 0 24 18"><rect x="1" y="1" width="22" height="16" fill="#d3ab35"/><path d="M1 1l11 9 11-9" fill="none" stroke="#121212" stroke-width="2"/></svg>info@ridgewaysecurity.example</div>
  <div class="label" style="margin-top:22px;margin-bottom:4px">ADDRESS:</div>
  <div style="line-height:20px">48 Harbor Lane<br>Millbrook, NH 03999</div>
</div>

<div class="abs field field-col" style="top:2913px"><svg width="11" height="11" viewBox="0 0 24 24"><circle cx="12" cy="8" r="5" fill="none" stroke="#d3ab35" stroke-width="2.5"/><path d="M3 23c0-6 4-9 9-9s9 3 9 9" fill="none" stroke="#d3ab35" stroke-width="2.5"/></svg>Name</div>
<div class="abs field field-col" style="top:2956px"><svg width="12" height="10" viewBox="0 0 24 18"><rect x="2" y="2" width="20" height="14" fill="none" stroke="#d3ab35" stroke-width="2.5"/><path d="M2 2l10 8 10-8" fill="none" stroke="#d3ab35" stroke-width="2.5"/></svg>Email</div>
<div class="abs field field-col" style="top:2999px"><svg width="9" height="12" viewBox="0 0 16 24"><rect x="2" y="1" width="12" height="22" rx="2" fill="none" stroke="#d3ab35" stroke-width="2.5"/></svg>Phone</div>
<div class="abs field field-comments"><svg width="11" height="11" viewBox="0 0 24 24"><rect x="2" y="2" width="20" height="20" fill="none" stroke="#d3ab35" stroke-width="2.5"/></svg>Comments</div>
<div class="abs btn-submit">Submit</div>

<div class="abs copyright">
  <span>Copyright © 2021 Ridgeway Security Group. All Rights Reserved</span>
  <span class="socials"><i></i><i></i></span>
</div>

</body>
</html>
```